C U B A N - C I G A R S - F L Y E R

I need a double-sided 5x7 club type flyer for a Memorial Day Weekend Trip.
The main side design needs to be similar to the attached flyer example. The front design of flyer is KEY. The design will be awarded to the closest finished submission to the example flyer.
Both sides of the flyer should also included event and business logo, which are also attached. Both logos can be altered to fit printing need accordingly.
Front side content is also attached.
The back side design will be very simple. Consists of 3 travel images and trip description, and my contact very details. Same color design as front. The attached word document contains backside details for REFERENCE ONLY. Please focus on front side when submitting a design for this project.
Target Market(s)
A F R I C A N - A M E R I C A N - C I G A R - S M O K E R S
Industry/Entity Type
Travel Industry
Requirements
Must have
- All the elements of the attached information
Nice to have
- Masculine Images
Should not have
- Large Cigar focus to catch customer's attention

```html
<!DOCTYPE html>
<html lang="en">
<head>
<meta charset="utf-8">
<title>Cuba Cigar Memorial Day Weekend Flyer</title>
<link rel="stylesheet" href="https://fonts.googleapis.com/css2?family=Saira:wght@300;400;500;600&family=Open+Sans:wght@400;700&display=swap">
<style>
:root{
  --page:#ffffff;
  --edge:#2a2522;
  --ink:#1d1d1f;
  --panel-top:#8ea9d2;
  --panel-bottom:#eaa7b1;
  --wood-dark:#1c130d;
  --wood-mid:#5b3a1f;
  --wood-warm:#9a6532;
  --amber:#c77a2a;
  --white:#ffffff;
  --note-bg:#d9d8d6;
  --rule:#3a3a3a;
}
*{margin:0;padding:0;box-sizing:border-box}
html,body{width:1200px;height:823px;overflow:hidden;background:var(--page)}
.canvas{position:relative;width:1200px;height:823px;font-family:"Saira",sans-serif;color:var(--ink)}
.side{position:absolute;top:0;height:818px;border:1.5px solid var(--edge);overflow:hidden}
.front{left:0;width:585px}
.back{left:615px;width:585px}
.scene{position:absolute;inset:0}
.front .scene{background:radial-gradient(ellipse 240px 280px at 440px 560px,var(--amber) 0%,rgba(150,90,40,.6) 35%,transparent 70%),linear-gradient(180deg,var(--wood-dark) 0%,var(--wood-mid) 45%,var(--wood-warm) 78%,#4a2f19 100%)}
.back .scene{background:radial-gradient(ellipse 300px 220px at 330px 330px,rgba(150,100,55,.55),transparent 70%),linear-gradient(180deg,#2a1c12 0%,#4a3220 40%,#1e150e 100%)}
.info-panel{position:absolute;left:45px;top:0;width:288px;height:818px;background:linear-gradient(180deg,var(--panel-top) 0%,#b3a8c5 60%,var(--panel-bottom) 100%);text-align:center}
.headline{position:absolute;left:20px;top:30px;text-align:left;font-weight:600;font-size:37px;line-height:45px;letter-spacing:.5px}
.tagline{position:absolute;left:18px;top:214px;font-size:17px;letter-spacing:.5px}
.rule{position:absolute;left:36px;width:215px;border-top:1px solid var(--rule)}
.pitch{position:absolute;left:0;width:288px;top:262px;font-size:22px;line-height:28px;font-weight:300;letter-spacing:.5px}
.details{position:absolute;left:0;width:288px;top:370px;font-size:14px;line-height:27.2px;font-weight:300}
.details .label{font-weight:600}
.call-to-act{position:absolute;left:0;width:288px;top:620px;font-size:30px;line-height:36px;font-weight:400}
.brand{position:absolute;left:0;width:288px;top:752px;display:flex;align-items:center;justify-content:center;gap:8px;font-size:15px;font-weight:500;color:#27305a}
.brand .dot{width:14px;height:14px;border-radius:50%;background:#27305a}
.event-badge{position:absolute;left:391px;top:32px;width:138px;height:138px;border-radius:50%;background:radial-gradient(circle,#e9e9ee 0%,#c9cad3 75%,rgba(200,200,210,.2) 100%);display:flex;align-items:center;justify-content:center;text-align:center;font-size:18px;font-weight:600;line-height:20px;color:#2b3d85}
.photo-strip{position:absolute;left:14px;top:12px;width:552px;height:124px;display:flex;gap:2px}
.photo-strip div{height:100%}
.ph-cars{width:171px;background:linear-gradient(135deg,#d8c39a 0%,#e3b43a 40%,#2e7fd0 75%,#3a3a3a 100%)}
.ph-map{width:187px;background:linear-gradient(160deg,#e8eef4 0%,#dbe5ef 55%,#f0a640 100%)}
.ph-cigars{width:190px;background:linear-gradient(135deg,#5a3216 0%,#9b5f34 45%,#c48a5c 70%,#6b3d1d 100%)}
.trip-note{position:absolute;left:14px;top:130px;width:552px;height:102px;background:var(--note-bg);padding:4px 6px;font-family:"Open Sans",sans-serif;font-size:7.9px;line-height:9.3px;text-align:justify;color:#222}
.pricing{position:absolute;left:21px;top:268px;color:var(--white);font-size:19px;line-height:26.6px;font-weight:300;letter-spacing:.6px}
.pricing b{font-weight:500}
.included{position:absolute;left:21px;top:480px;color:var(--white);font-size:19px;line-height:26.6px;font-weight:300;letter-spacing:.6px}
.included h2{font-size:19px;font-weight:500;margin-left:11px}
.included .indent{padding-left:11px}
.sign-off{position:absolute;left:435px;top:739px;width:131px;height:57px;border-radius:8px;background:rgba(255,255,255,.85);display:flex;align-items:center;justify-content:space-around;font-size:9px;font-weight:500;color:#27305a;text-align:center;line-height:11px}
.sign-off .split{width:1px;height:40px;background:#27305a}
</style>
</head>
<body>
<main class="canvas">

  <section class="side front">
    <div class="scene" role="img" aria-label="Photo of a snifter of brandy and two lit cigars on a rustic wooden table with drifting smoke"></div>

    <div class="info-panel">
      <h1 class="headline">A Cuba Cigar<br>Gentlemen’s<br>Memorial Day<br>Weekend</h1>
      <p class="tagline">Cigars, Rum &amp; Classic Cars...</p>
      <div class="rule" style="top:251px"></div>
      <p class="pitch">Legally travel to<br>Cuba &amp; return with real<br>CUBAN CIGARS!</p>
      <div class="rule" style="top:358px"></div>
      <div class="details">
        <p class="label">Trip Name</p>
        <p>Rum Cigars and Classic Cars</p>
        <p class="label">MEMORIAL DAY WEEKEND 2018!</p>
        <p class="label">Dates</p>
        <p>Friday, May 25th-Tuesday May 29th</p>
        <p class="label">Book Today at</p>
        <p>www.mywebsite.com/CUBA2018</p>
        <p class="label">For More Information</p>
        <p>Call: xxx-xxx-xxxx</p>
      </div>
      <p class="call-to-act">Book Now!<br>Space is Limited</p>
      <div class="brand"><span class="dot"></span>Harbor Travel Co</div>
    </div>

    <div class="event-badge">Harbor<br>Weekend</div>
  </section>

  <section class="side back">
    <div class="scene" role="img" aria-label="Dark blurred photo of a wooden table surface"></div>

    <div class="photo-strip">
      <div class="ph-cars" role="img" aria-label="Photo of colorful classic American cars parked in Havana"></div>
      <div class="ph-map" role="img" aria-label="Map of the flight route from Miami to Havana, Cuba"></div>
      <div class="ph-cigars" role="img" aria-label="Close-up photo of hand-rolled Cuban cigars"></div>
    </div>

    <p class="trip-note">Cuba is the ultimate bucket list destination for any cigar lover. Now is your opportunity to legally travel to Cuba and experience a country that has been off limits to Americans for more than 50 years before it changes. Smoke fine Cuban cigars, meet its resilient people and experience Cuba's fascinating culture. Tour cigar factories, watch expert cigar rollers, visit a humidor factory and workshop, tour the Old Harbor Rum Museum to learn firsthand the process of making rum followed by rum tasting and pairings with Cuban cigars in a private setting and much more. Explore the Pinar Del Rio located in the Viñales Valley known for its stunning landscapes and tobacco plantations. Visit the famous Vega Verde Tobacco Farm to see first hand where and how the tobacco process is grown for fine Cuban Cigars. The bucket list trip of a lifetime awaits on this 'people to people' Cigar Journey to Cuba to learn first hand about Cuban cigars, meet the Cuban people, experience incredible cuisine, drive in classic American cars along the Malecon and experience the Cuban cigar process from <b><i>'seed to smoke'</i></b> and an opportunity to smoke in the birthplace of cigars!</p>

    <div class="pricing">
      <p><b>Trip Cost:</b> $2050</p>
      <p><b>Deposit:</b> $300</p>
      <p>Payment plans available</p>
      <p>$300 Deposit Required</p>
      <p>Final payment Due By April 10, 2018</p>
      <p>*NON-REFUNDABLE</p>
      <p>*Passport Required</p>
    </div>

    <div class="included">
      <h2>What's Included:</h2>
      <p>- 4 Days / 3 Nights</p>
      <p>- 5 Star Hotel Accommodations Based on Double Occupancy</p>
      <p>- Roundtrip Coastal Air Tickets from</p>
      <p class="indent">Fort Lauderdale Florida - Cuba</p>
      <p>- Tour Bus Chauffeured Transportation</p>
      <p>- All Rum and Cigar Tour Events</p>
      <p>- Select Meals (Breakfast, Welcome and Farewell Dinner)</p>
      <p class="indent">and More!</p>
    </div>

    <div class="sign-off">
      <span>Harbor<br>Travel Co</span>
      <span class="split"></span>
      <span>Harbor<br>Weekend</span>
    </div>
  </section>

</main>
</body>
</html>
```